Logo Design with Business Card Project

Attractive Logo with colourful background !
I have uploaded a new image of the updated Home page with the Real Estate landing page for your reference.
We are looking for a Business card design which easily identifies us as a Video classifieds company.

Target Market(s)

20 - 35 yr old people who are connected through social media

Industry/Entity Type

Business

Logo Text

WE SEE ALL

Logo styles of interest
Abstract Logo
Requirements
Must have
• Simple layout with striking / engaging colours
Nice to have
• Require an updated logo to go on business card / home page

```html
<!DOCTYPE html>
<html lang="en">
<head>
<meta charset="utf-8">
<title>WE SEE ALL – Business Card</title>
<link rel="stylesheet" href="https://fonts.googleapis.com/css2?family=Anton&family=Roboto:wght@400;700;900&display=swap">
<style>
  :root {
    --backdrop: #c6c6c6;
    --card: #262626;
    --card-band: #2e2d2b;
    --white: #ffffff;
    --sky: #1ba4e2;
    --amber: #e9a41e;
  }
  * { margin: 0; padding: 0; box-sizing: border-box; }
  html, body { width: 1200px; height: 900px; overflow: hidden; }
  body {
    background: var(--backdrop);
    font-family: "Roboto", Arial, sans-serif;
    position: relative;
  }
  .card {
    position: absolute;
    top: 300px;
    width: 525px;
    height: 300px;
    background: var(--card);
    box-shadow: 0 6px 14px rgba(0,0,0,0.25);
    overflow: hidden;
  }
  .card--front { left: 50px; }
  .card--back { left: 625px; }

  .front-bands { position: absolute; inset: 0; }

  .brand {
    position: absolute;
    left: 42px;
    top: 64px;
    display: flex;
    align-items: center;
    gap: 12px;
  }
  .brand__mark {
    width: 26px; height: 26px;
    background: var(--sky);
  }
  .brand__name {
    font-weight: 900;
    font-size: 40px;
    color: var(--white);
    letter-spacing: 0.5px;
    line-height: 1;
  }

  .contact {
    position: absolute;
    left: 42px;
    top: 140px;
    color: var(--white);
  }
  .contact__name {
    color: var(--sky);
    font-weight: 700;
    font-size: 18px;
    letter-spacing: 0.5px;
    text-transform: uppercase;
  }
  .contact__role {
    font-weight: 700;
    font-size: 13px;
    margin-top: 2px;
  }
  .contact__lines {
    margin-top: 18px;
    font-size: 14px;
    font-weight: 700;
    line-height: 1.45;
  }
  .contact__label { color: var(--amber); }
  .contact__gap { margin-left: 10px; }

  .pitch {
    position: absolute;
    inset: 0;
    display: flex;
    flex-direction: column;
    align-items: center;
    justify-content: center;
    font-family: "Anton", "Impact", sans-serif;
    text-align: center;
  }
  .pitch__headline {
    color: var(--white);
    font-size: 42px;
    line-height: 1.05;
  }
  .pitch__sub {
    color: var(--white);
    font-size: 19px;
    letter-spacing: 0.5px;
    line-height: 1.3;
  }
  .pitch__highlight { color: var(--amber); }
  .pitch__url {
    color: var(--sky);
    font-size: 60px;
    line-height: 1.15;
    margin-top: 4px;
  }
</style>
</head>
<body>
  <section class="card card--front">
    <svg class="front-bands" width="525" height="300" viewBox="0 0 525 300" aria-hidden="true">
      <rect x="250" y="0" width="40" height="300" fill="var(--card-band)"/>
      <rect x="300" y="60" width="40" height="240" fill="var(--card-band)"/>
      <rect x="350" y="20" width="40" height="280" fill="var(--card-band)"/>
      <rect x="400" y="110" width="40" height="190" fill="var(--card-band)"/>
      <rect x="450" y="160" width="40" height="140" fill="var(--card-band)"/>
    </svg>
    <div class="brand">
      <span class="brand__mark"></span>
      <span class="brand__name">WE SEE ALL</span>
    </div>
    <div class="contact">
      <p class="contact__name">Daniel Hartwell</p>
      <p class="contact__role">Managing Director</p>
      <div class="contact__lines">
        <p><span class="contact__label">PH:</span> + 617 5550 1846 <span class="contact__label contact__gap">M:</span> 0400 555 017</p>
        <p><span class="contact__label">E:</span> daniel@weseeall.com</p>
      </div>
    </div>
  </section>

  <section class="card card--back">
    <div class="pitch">
      <p class="pitch__headline">Buy and Sell</p>
      <p class="pitch__sub">through the <span class="pitch__highlight">#1 Video Classifieds</span></p>
      <p class="pitch__url">www.WeSeeAll.com</p>
    </div>
  </section>
</body>
</html>
```